International Used Food Processing Equipment company needs an awesome website!

We have been in business now for more than 15 years, and we are now launching a new website where international and USA based customers can view photos, descriptions, and ask questions of industrial food processing equipment.

We want the site to be vibrant and but yet communicate a professional tone to our customers. Most of our customers are older males, and the site must be easy to navigate, with easy on the eye color scheme. We want to features a lot of photos and a excellent equipment descriptions, with links where visitors can click on an item to send us a request for more information. We require easy to read font, clear navigation buttons and clear contact information to be found on each page.

Some of our competitors sites:
www.KVPTrade.com
www.lantorvalleyworks.com
www.pelvoxgroup.com

Our business name and logo is attached, but this is a rending of an image that was made about 10 years ago. Please let us know if you have any questions.

Target Market(s)

Food processing companies (canneries, fresh cut sector, large catering companies) in the USA and South America.

Logo Text

Excellent Machines at Excellent Prices

Coding

Coded - Design and coding required

Number of Pages Required

5+ page

Colors

Designer to choose colors to be used in the design.

Requirements
Must have
• Easy to navigate photo galleries, easy category search and easy machine search by keywords.
• Event Calendar
• Sign-up page for email newsletter
Nice to have
• Blog feature or latest news
• Past projects page
Should not have
• Hard to read font

```html
<!DOCTYPE html>
<html lang="en">
<head>
<meta charset="utf-8">
<title>The Plant Steward – Industrial Food Processing Equipment</title>
<link href="https://fonts.googleapis.com/css2?family=Montserrat:wght@400;500;600;700&family=Open+Sans:wght@400;600&display=swap" rel="stylesheet">
<style>
:root{
  --green:#5aa82c;
  --green-dark:#4a9123;
  --orange:#f6a01a;
  --ink:#333333;
  --muted:#777777;
  --light:#f2f2f2;
  --footer:#3a3a3a;
  --footer-deep:#262626;
  --white:#ffffff;
}
*{margin:0;padding:0;box-sizing:border-box}
html,body{width:1200px;height:2927px;overflow:hidden}
body{position:relative;font-family:"Open Sans",Arial,sans-serif;color:var(--ink);background:var(--white)}
.abs{position:absolute}
h2.section-title{position:absolute;left:0;width:1200px;text-align:center;font-family:"Montserrat",Arial,sans-serif;font-weight:400;font-size:25px;color:var(--ink)}
.divider{position:absolute;left:552px;width:96px;height:2px;background:var(--green)}
.divider::after{content:"";position:absolute;left:44px;top:-3px;width:8px;height:8px;background:var(--orange);transform:rotate(45deg)}
.lead{position:absolute;left:250px;width:700px;text-align:center;font-size:12.5px;line-height:21px;color:#555}

/* hero */
.hero{left:0;top:0;width:1200px;height:708px;background:radial-gradient(ellipse at 70% 30%,#7d7257 0%,#4a4a34 35%,#2b3324 70%,#1c2418 100%)}
.hero-shade{left:0;top:0;width:1200px;height:708px;background:linear-gradient(90deg,rgba(40,90,40,.35),rgba(0,0,0,.1) 50%,rgba(30,110,50,.35))}
.logo-diamond{left:488px;top:103px;width:224px;height:224px;background:var(--white);transform:rotate(45deg);border:3px solid #ddd;box-shadow:0 0 0 6px rgba(255,255,255,.35)}
.logo-name{left:450px;top:193px;width:300px;text-align:center;font-family:"Montserrat",Arial,sans-serif;font-weight:700;font-size:17px;color:#222;line-height:22px}
.hero-title{left:0;top:420px;width:1200px;text-align:center;color:var(--white);font-family:"Montserrat",Arial,sans-serif}
.hero-title .l1{display:block;font-size:25px;font-weight:400;letter-spacing:.5px}
.hero-title .l2{display:block;font-size:17px;font-weight:700;margin-top:4px}
.btn{display:block;text-align:center;font-family:"Montserrat",Arial,sans-serif;font-weight:500;color:var(--white)}
.hero-btn{left:530px;top:512px;width:140px;height:38px;line-height:38px;background:var(--green);font-size:12px}
.socials{display:flex;gap:20px}
.social{width:28px;height:28px;background:var(--white);transform:rotate(45deg);position:relative}
.social::after{content:"";position:absolute;left:9px;top:9px;width:10px;height:10px;border-radius:50%;background:var(--green)}
.hero-socials{left:506px;top:608px}

/* nav */
.nav{left:0;top:708px;width:1200px;height:57px;background:var(--green)}
.nav ul{list-style:none}
.nav li{position:absolute;top:0;height:57px;display:flex;align-items:center;font-family:"Montserrat",Arial,sans-serif;font-weight:600;font-size:11px;color:var(--white);white-space:nowrap}
.nav-phone{left:855px;top:0;width:183px;height:57px;background:var(--orange);color:var(--white);font-family:"Montserrat",Arial,sans-serif;font-weight:600;font-size:13px;display:flex;align-items:center;justify-content:center;gap:10px}

/* services */
.service{width:220px;text-align:center}
.service .ring{width:94px;height:94px;margin:0 auto;border:2px solid var(--green);border-radius:50%}
.service h3{margin-top:22px;font-weight:600;font-size:14px;line-height:20px;color:var(--ink);height:40px}
.service p{margin-top:10px;font-size:11px;line-height:16px;color:var(--muted);height:48px;overflow:hidden}
.service .more{margin:23px auto 0;width:92px;height:29px;line-height:29px;font-size:11px;background:#ececec;color:#666;font-family:"Open Sans",Arial,sans-serif}
.service .more.active{background:var(--orange);color:var(--white)}

/* how it works */
.how-text{left:162px;top:1236px;width:425px;font-size:12px;line-height:19px;color:#666}
.how-text p{margin-bottom:10px}
.checklist{left:162px;top:1391px;display:grid;grid-template-columns:200px 200px;row-gap:3px;font-size:10.5px;color:#777;list-style:none}
.checklist li{display:flex;align-items:center;gap:10px;height:20px}
.video-btn{left:162px;top:1504px;width:142px;height:37px;line-height:37px;background:var(--orange);font-size:11px;font-weight:600}
.video-frame{left:624px;top:1266px;width:391px;height:275px;border:7px solid var(--green)}
.video-media{left:646px;top:1243px;width:392px;height:279px;background:radial-gradient(circle at 60% 40%,#6b6458,#3a362f 55%,#1f1d1a)}
.video-label{left:646px;top:1334px;width:392px;text-align:center;color:var(--white);font-weight:600;font-size:14px}

/* features */
.features{left:0;top:1590px;width:1200px;height:445px;background:linear-gradient(90deg,#2a2520,#4a4038 35%,#3b352f 65%,#2b2a28)}
.features .section-title{color:var(--white)}
.feature{width:268px;height:280px;border:3px solid var(--green);padding:8px}
.feature .media{width:100%;height:100%;position:relative}
.feature .caption{position:absolute;left:0;bottom:0;width:100%;height:52px;background:rgba(0,0,0,.55);color:var(--white);font-family:"Montserrat",Arial,sans-serif;font-size:19px;line-height:52px;padding-left:10px;letter-spacing:.5px}

/* blog */
.blog{left:0;top:2035px;width:1200px;height:570px;background:var(--light)}
.post{position:absolute;width:268px;height:281px;overflow:hidden}
.post .photo{position:absolute;inset:0}
.post .shade{position:absolute;left:0;bottom:0;width:100%;height:110px;background:linear-gradient(180deg,rgba(0,0,0,0),rgba(0,0,0,.8))}
.post .text{position:absolute;left:14px;right:12px;bottom:12px;color:var(--white)}
.post h4{font-weight:400;font-size:15px;margin-bottom:6px}
.post p{font-size:10.5px;line-height:15px}
.post time{display:block;margin-top:6px;font-size:10px;color:var(--orange)}
.dots{left:576px;display:flex;gap:6px}
.dots span{width:11px;height:11px;border-radius:50%;background:var(--green)}
.dots span:first-child{background:var(--orange)}

/* footer */
.footer{left:0;top:2605px;width:1200px;height:273px;background:var(--footer);color:#eee}
.footer h5{font-family:"Montserrat",Arial,sans-serif;font-weight:500;font-size:14px;color:var(--white);margin-bottom:24px}
.footer ul{list-style:none;font-size:11px;line-height:21px;color:#ddd}
.contact li{display:flex;gap:12px;align-items:flex-start;margin-bottom:8px;line-height:16px}
.contact svg{flex:none;margin-top:1px}
.form input,.form .msg{display:block;width:234px;height:27px;background:var(--white);border:1px solid #ccc;font-size:10.5px;color:#666;padding:6px 8px;margin-bottom:4px;font-family:"Open Sans",Arial,sans-serif}
.form .msg{height:56px}
.form .submit{width:92px;height:28px;line-height:28px;background:var(--orange);font-size:11px;margin-top:8px}
.footer-socials{left:586px;top:2816px;gap:18px}
.footer-socials .social{width:22px;height:22px}
.footer-socials .social::after{left:6px;top:6px;width:8px;height:8px}
.copyright{left:0;top:2878px;width:1200px;height:49px;line-height:49px;background:var(--footer-deep);color:#ccc;text-align:center;font-size:10.5px}
</style>
</head>
<body>

<!-- Hero -->
<div class="abs hero" role="img" aria-label="Close-up photograph of industrial food processing machinery with green metal frame"></div>
<div class="abs hero-shade"></div>
<div class="abs logo-diamond"></div>
<div class="abs logo-name">The Plant Steward<br>Used Food Machinery</div>
<div class="abs hero-title"><span class="l1">EVERYTHING YOU NEED TO START A NEW</span><span class="l2">INDUSTRIAL FOOD PROCESSING EQUIPMENT</span></div>
<a class="abs btn hero-btn">VIEW PRODUCTS</a>
<div class="abs socials hero-socials"><span class="social"></span><span class="social"></span><span class="social"></span><span class="social"></span></div>

<!-- Navigation -->
<nav class="abs nav">
  <ul>
    <li style="left:162px"><svg width="20" height="18" viewBox="0 0 20 18"><path d="M10 1 1 9h3v8h4v-5h4v5h4V9h3z" fill="#fff"/></svg></li>
    <li style="left:218px">COMPANY</li>
    <li style="left:320px">PRODUCTS</li>
    <li style="left:423px">SECTORS</li>
    <li style="left:517px">SERVICES</li>
    <li style="left:611px">REFERENCES</li>
    <li style="left:724px">CONTACT US</li>
  </ul>
  <div class="abs nav-phone"><svg width="18" height="14" viewBox="0 0 18 14"><path d="M1 4c0-3 16-3 16 0v2h-4V4H5v2H1zM4 7h10l2 6H2z" fill="#fff"/></svg>00 33-100-555-014</div>
</nav>

<!-- Services -->
<div class="abs service" style="left:151px;top:808px"><div class="ring"></div><h3>Electrical &amp; mechanical<br>assembly</h3><p>We perform or supervise every step of your project from assembly to final commissioning.</p><a class="btn more active">Read More</a></div>
<div class="abs service" style="left:378px;top:808px"><div class="ring"></div><h3>Engineering - Audit<br>Systems</h3><p>Visit of engineers specialized in powder handling on your production site to optimize your process line</p><a class="btn more">Read More</a></div>
<div class="abs service" style="left:606px;top:808px"><div class="ring"></div><h3>Test Plant</h3><p>The test center VELMARK PROCESS has been built for all of our industrial customers desiring to define the</p><a class="btn more">Read More</a></div>
<div class="abs service" style="left:832px;top:808px"><div class="ring"></div><h3>Management of<br>your project</h3><p>The Plant Steward coordinates all services to handle your whole project from pre-study to operations, through</p><a class="btn more">Read More</a></div>

<!-- How it works -->
<h2 class="section-title" style="top:1100px">How The Plant Steward Works</h2>
<div class="divider" style="top:1141px"></div>
<p class="lead" style="top:1162px">The Plant Steward Process is "The smartest designer for powder handling solutions" for bulk handling system and the realization of your production lines from conception to commissioning internationally.</p>
<div class="abs how-text">
  <p>Our many years of experience in food and feed, chemical and fine chemical processing industries, water treatment and building industry allow us to offer you the benefits of inter-sector synergy.</p>
  <p>Our industrial workshop allows you to perform tests on our test plant and guarantees the success of your project and the reliability of your production line. Our human size structure offers excellent flexibility and reactivity with competitive budgets.</p>
</div>
<ul class="abs checklist">
  <li><svg width="12" height="10"><path d="M1 5h9M6 1l4 4-4 4" stroke="#5aa82c" stroke-width="1.5" fill="none"/></svg>FIBC SOLUTIONS</li>
  <li><svg width="12" height="10"><path d="M1 5h9M6 1l4 4-4 4" stroke="#5aa82c" stroke-width="1.5" fill="none"/></svg>LUMPBREAKING - MILLING</li>
  <li><svg width="12" height="10"><path d="M1 5h9M6 1l4 4-4 4" stroke="#5aa82c" stroke-width="1.5" fill="none"/></svg>SACK SOLUTIONS</li>
  <li><svg width="12" height="10"><path d="M1 5h9M6 1l4 4-4 4" stroke="#5aa82c" stroke-width="1.5" fill="none"/></svg>SIEVE MACHINE</li>
  <li><svg width="12" height="10"><path d="M1 5h9M6 1l4 4-4 4" stroke="#5aa82c" stroke-width="1.5" fill="none"/></svg>DRUM SOLUTIONS</li>
  <li><svg width="12" height="10"><path d="M1 5h9M6 1l4 4-4 4" stroke="#5aa82c" stroke-width="1.5" fill="none"/></svg>STORAGE</li>
  <li><svg width="12" height="10"><path d="M1 5h9M6 1l4 4-4 4" stroke="#5aa82c" stroke-width="1.5" fill="none"/></svg>CONVEYING SYSTEM</li>
</ul>
<a class="abs btn video-btn">WATCH VIDEO</a>
<div class="abs video-frame"></div>
<div class="abs video-media" role="img" aria-label="Video still of pressure gauges on processing equipment"></div>
<svg class="abs" style="left:812px;top:1338px" width="60" height="60" viewBox="0 0 60 60"><circle cx="30" cy="30" r="27" stroke="#fff" stroke-width="3" fill="none"/><path d="M25 18l12 12-12 12" stroke="#fff" stroke-width="4" fill="none"/></svg>
<div class="abs video-label" style="top:1407px">Watch overview</div>

<!-- Features -->
<section class="abs features" role="img" aria-label="Blurred photograph of a chef in a commercial kitchen">
  <h2 class="section-title" style="top:36px">Our Features</h2>
  <div class="divider" style="top:74px"></div>
  <div class="abs feature" style="left:160px;top:121px"><div class="media" role="img" aria-label="Photograph of a commercial espresso machine" style="background:linear-gradient(160deg,#6a3e22,#2d1d14 60%,#a3622e)"><div class="caption">PRODUCTS</div></div></div>
  <div class="abs feature" style="left:466px;top:121px"><div class="media" role="img" aria-label="Photograph of cooks working in a restaurant kitchen" style="background:linear-gradient(160deg,#c9c3b8,#7a6b5b 50%,#3d3a36)"><div class="caption">INDUSTRIES</div></div></div>
  <div class="abs feature" style="left:771px;top:121px"><div class="media" role="img" aria-label="Photograph of a team meeting in an office" style="background:linear-gradient(160deg,#2f3a44,#556068 45%,#b9a98f)"><div class="caption">SERVICES</div></div></div>
</section>

<!-- Blog -->
<section class="abs blog">
  <h2 class="section-title" style="top:40px">Latest Blog</h2>
  <div class="divider" style="top:78px"></div>
  <p class="lead" style="top:117px">The Plant Steward Process is "The smartest designer for powder handling solutions" for bulk handling system and the realization of your production lines from conception to commissioning internationally.</p>
  <article class="post" style="left:160px;top:195px"><div class="photo" role="img" aria-label="Photograph of lettuce seedlings growing in hydroponic trays" style="background:linear-gradient(180deg,#dfe8d8,#7fb152 55%,#3e6b22)"></div><div class="shade"></div><div class="text"><h4>Blog Title Will be Here</h4><p>Our many years of experience in food and feed, chemical and fine chemical processing industries, water treatment and building industry</p><time>January 15, 2019</time></div></article>
  <article class="post" style="left:466px;top:195px"><div class="photo" role="img" aria-label="Photograph of a worker with gloves cleaning a workbench" style="background:linear-gradient(160deg,#2a3a5a,#6b5a44 50%,#c9a23c)"></div><div class="shade"></div><div class="text"><h4>Blog Title Will be Here</h4><p>Our many years of experience in food and feed, chemical and fine chemical processing industries, water treatment and building industry</p><time>January 15, 2019</time></div></article>
  <article class="post" style="left:771px;top:195px"><div class="photo" role="img" aria-label="Photograph of a chef plating a dish" style="background:linear-gradient(160deg,#d9d2c8,#9a7a5e 50%,#3a2c22)"></div><div class="shade"></div><div class="text"><h4>Blog Title Will be Here</h4><p>Our many years of experience in food and feed, chemical and fine chemical processing industries, water treatment and building industry</p><time>January 15, 2019</time></div></article>
  <div class="abs dots" style="top:511px"><span></span><span></span><span></span></div>
</section>

<!-- Footer -->
<footer class="abs footer">
  <div class="abs" style="left:160px;top:36px"><h5>Industrial Sector</h5><ul><li>Food and Feed</li><li>Chemical processing industry</li><li>Fine chemical processing<br>industry</li><li>Building industry</li><li>Waste water treatment</li></ul></div>
  <div class="abs" style="left:406px;top:36px"><h5>Quick Links</h5><ul><li>Home</li><li>Company</li><li>products</li><li>Sectors</li><li>Services</li><li>References</li><li>Contact Us</li></ul></div>
  <div class="abs" style="left:579px;top:36px;width:200px"><h5>Contact Us</h5><ul class="contact">
    <li><svg width="10" height="14" viewBox="0 0 10 14"><path d="M5 0a5 5 0 0 0-5 5c0 4 5 9 5 9s5-5 5-9a5 5 0 0 0-5-5zm0 7a2 2 0 1 1 0-4 2 2 0 0 1 0 4z" fill="#fff"/></svg><span>Rue des Ateliers - Z.A du Pont Vert<br>35510 Levray - France</span></li>
    <li><svg width="10" height="12" viewBox="0 0 10 12"><path d="M2 0h2l1 3-1.5 1.5a7 7 0 0 0 3 3L8 6l2 1v2c0 2-2 3-4 2S0 6 0 3 1 0 2 0z" fill="#fff"/></svg><span>+33 (0)1 00 55 50 14</span></li>
    <li><svg width="12" height="9" viewBox="0 0 12 9"><rect width="12" height="9" fill="#fff"/><path d="M0 0l6 5 6-5" stroke="#3a3a3a" fill="none"/></svg><span>contact@plantsteward.com</span></li>
  </ul></div>
  <div class="abs form" style="left:804px;top:36px"><h5>Get In Touch</h5><input value="Name" readonly><input value="Email" readonly><div class="msg">Message</div><a class="btn submit">Submit</a></div>
</footer>
<div class="abs socials footer-socials"><span class="social"></span><span class="social"></span><span class="social"></span><span class="social"></span></div>
<div class="abs copyright">Copyright © 2019 The Plant Steward - All rights reserved</div>

</body>
</html>
```